Signage Design Project

Busisness is a bakery and deli long time owned by the Tavel family. Want to develop a new outside sign that communicates it is a deli and a bakery but keeps the tavel name in the design.

The sign when produced will be about 10' by 3' . It is not lighted at present but could be if it were advantageous.

The name of the store is:

Tavel's Hudson Bakery and Deli. The concept is to have a new,modern sign that reinforces that it is a deli and a bakery, as most people only know about the bakery side of the business
Updates

The name Tavel is just a reinforcer so the people kno it is still in the family.  The emphasis should be on the HUDSON BAKERY and DELI

Target Market(s)

Small business breakfast and lunch customers

Industry/Entity Type

Bakery

Requirements
Must have
• Great impact from the road. Communicate that it is a deli and a bakery. Keep the Tavel name but need not be a major design element

```html
<!DOCTYPE html>
<html lang="en">
<head>
<meta charset="utf-8">
<title>Tavel's Hudson Bakery and Deli – Sign</title>
<link rel="stylesheet" href="https://fonts.googleapis.com/css2?family=Righteous&display=swap">
<style>
  :root {
    --sign-blue: #0f4e9f;
    --ornament-blue: #2a66b3;
    --lettering: #fcc10f;
  }
  html, body {
    margin: 0;
    padding: 0;
    width: 1200px;
    height: 360px;
    overflow: hidden;
    background: var(--sign-blue);
  }
  .sign {
    position: relative;
    width: 1200px;
    height: 360px;
    background: var(--sign-blue);
    overflow: hidden;
  }
  .sign__ornament {
    position: absolute;
    top: 14px;
    width: 56px;
    height: 332px;
    border-radius: 28px;
    background: linear-gradient(180deg, rgba(42,102,179,0.25), rgba(42,102,179,0.5), rgba(42,102,179,0.25));
  }
  .sign__ornament--left { left: 14px; }
  .sign__ornament--right { right: 14px; }
  .sign__name {
    margin: 0;
    font-family: "Righteous", sans-serif;
    font-weight: 400;
    color: var(--lettering);
  }
  .sign__family,
  .sign__place,
  .sign__trade {
    position: absolute;
    display: block;
    line-height: 1;
    white-space: nowrap;
  }
  .sign__family {
    left: 192px;
    top: 112px;
    font-size: 50px;
  }
  .sign__place {
    left: 418px;
    top: 42px;
    font-size: 150px;
  }
  .sign__trade {
    left: 0;
    right: 0;
    top: 198px;
    text-align: center;
    font-size: 126px;
  }
</style>
</head>
<body>
  <div class="sign">
    <div class="sign__ornament sign__ornament--left" role="img" aria-label="Vertical scroll ornament in light blue"></div>
    <div class="sign__ornament sign__ornament--right" role="img" aria-label="Vertical scroll ornament in light blue"></div>
    <h1 class="sign__name">
      <span class="sign__family">Tavel's</span>
      <span class="sign__place">Hudson</span>
      <span class="sign__trade">Bakery and Deli</span>
    </h1>
  </div>
</body>
</html>
```